Landing Page and Logo for Auto-Blogging Platform

I created a platform that allows users to start a blog for their business, hobby, charity, etc. I need a landing page where users can learn about the platform, benefits of consistent blogging, SEO value, plans/pricing, etc. The landing page needs to have multiple call to action buttons encouraging the visitor to register/sign up for a free trial.

In addition to the landing page, I need a page for users to establish the settings for their blog. This page should be a fairly simple form, intended for the user to enter a few details to set up their blog:
1. Name of Blog
2. Up to 10 topics and/or keywords the blog should focus on
3. Theme: Color-scheme and logo upload for blog.

I have attached the specifications of the platform's functionality so you can better understand how it works, plans/pricing, etc.

I also need a logo for the business. The name of the platform is PostNook.

Target Market(s)

Website owners, bloggers, business owners

Industry/Entity Type

Technology, Internet, web design

Coding

Coded - Design and coding required

Number of Pages Required

2 page

Colors
0054AA
0677BA
7BADD7
CADEEF
E8F1F8
0094D4
00A9DD
6FCCEA
C7EBF8
E9F6FB

Requirements
Must have
• Eye-catching design but fairly light on content (keep it simple and brief.)
Nice to have
• Eye-catching yet simple design, clean and easy to understand what we are offering.
Should not have
• Too much “wordy” and confusing content.

```html
<!DOCTYPE html>
<html lang="en">
<head>
<meta charset="utf-8">
<title>PostNook – Your Voice, Your Platform, Your Story</title>
<link rel="stylesheet" href="https://fonts.googleapis.com/css2?family=Poppins:wght@400;500;600;700&display=swap">
<style>
:root{
  --blue:#0054aa;
  --blue-mid:#0677ba;
  --sky:#0094d4;
  --sky-bright:#00a9dd;
  --sky-soft:#7badd7;
  --sky-pale:#cadeef;
  --tint:#e8f1f8;
  --tint-2:#e9f6fb;
  --ink:#222;
  --text:#333;
  --dark:#333333;
  --footer:#2b2b2b;
  --white:#fff;
  --star:#f7b500;
  --orange:#f6b133;
}
*{box-sizing:border-box;margin:0;padding:0}
html,body{width:1200px;height:4252px;overflow:hidden}
body{font-family:'Poppins',sans-serif;color:var(--text);background:var(--white);position:relative}
section,header,footer{position:absolute;left:0;width:1200px}
.btn{position:absolute;display:flex;align-items:center;justify-content:center;background:var(--blue);color:var(--white);font-size:14px;font-weight:500;text-decoration:none;height:40px;width:210px}
.btn--light{background:var(--white);color:var(--ink)}
.art{position:absolute;border-radius:16px}
.rule{display:block;width:60px;height:3px;background:var(--sky);margin-top:12px}
.title{font-size:30px;font-weight:700;color:var(--ink);line-height:1.2}
.title em{font-style:normal;color:var(--sky)}

/* header + hero */
.hero{top:0;height:676px;background:linear-gradient(120deg,#eaf5fb 0%,#e3f1fa 60%,#eef7fc 100%);overflow:hidden}
.brand{position:absolute;left:143px;top:30px;font-size:31px;font-weight:700;color:var(--blue);letter-spacing:.5px}
.btn--signup{left:950px;top:28px;width:108px;height:42px;font-size:14px}
.hero__title{position:absolute;left:143px;top:262px;font-size:40px;font-weight:700;color:var(--blue);line-height:1.45}
.hero .btn{left:142px;top:404px}
.hero__art{left:615px;top:160px;width:470px;height:345px;background:linear-gradient(160deg,#cfe5f6,#5aa4e4 60%,#2c3a8c)}
.hero__wave{position:absolute;left:0;bottom:0;width:1200px;height:90px}

/* about */
.about{top:676px;height:600px}
.about__art{left:142px;top:74px;width:428px;height:438px;background:linear-gradient(150deg,#eef4fa,#b9d6f0 55%,#f5b64a)}
.about__body{position:absolute;left:643px;top:110px;width:405px}
.about__body p{margin-top:38px;font-size:12.4px;line-height:1.55;color:#333}
.about .btn{left:643px;top:426px}

/* how it works */
.how{top:1276px;height:764px;background:var(--blue);color:var(--white);text-align:center}
.how .title{color:var(--white);position:absolute;top:78px;width:100%}
.how .rule{margin:12px auto 0}
.how__lead{position:absolute;top:160px;left:300px;width:600px;font-size:12.5px;line-height:1.55}
.step{position:absolute;width:200px;margin-left:-100px}
.step__icon{width:92px;height:92px;border-radius:50%;background:var(--white);margin:0 auto;display:flex;align-items:center;justify-content:center}
.step__name{margin-top:18px;font-size:18px;font-weight:600;line-height:1.5}
.how .btn{left:495px;top:635px}

/* benefits */
.benefits{top:2040px;height:564px}
.benefits__body{position:absolute;left:142px;top:98px}
.ticks{position:absolute;list-style:none;font-size:12.5px;font-weight:500;color:var(--ink)}
.ticks li{display:flex;align-items:center;height:34px}
.ticks svg{margin-right:12px;flex:none}
.benefits .btn{left:142px;top:435px}
.benefits__art{left:643px;top:90px;width:414px;height:400px;background:linear-gradient(160deg,#fff6e4,#f7c35c 40%,#4a9ae0 80%,#222)}

/* seo */
.seo{top:2604px;height:553px;background:var(--tint-2)}
.seo__art{left:143px;top:77px;width:418px;height:388px;background:linear-gradient(150deg,#e8f4fb,#7bb7e8 55%,#f5b44a)}
.seo .title{position:absolute;left:642px;top:110px}
.seo .btn{left:642px;top:386px}

/* pricing */
.pricing{top:3157px;height:600px;background:var(--dark);color:var(--white);text-align:center}
.pricing .title{color:var(--white);position:absolute;top:68px;width:100%}
.pricing .rule{margin:12px auto 0}
.pricing__lead{position:absolute;left:280px;top:162px;width:640px;font-size:12.5px;line-height:1.55}
.plans{position:absolute;left:272px;top:232px;width:656px;display:flex;background:#eaf5fb}
.plan{flex:1;border-right:1px solid #cfdbe6;height:196px}
.plan:last-child{border-right:none}
.plan__name{background:var(--blue);height:38px;line-height:38px;font-size:17px;font-weight:600;border-right:1px solid #3d7bc2}
.plan__desc{color:#333;font-size:12.5px;line-height:1.5;margin-top:26px}
.plan__price{color:var(--sky);font-size:22px;font-weight:600;margin-top:8px}
.plan__price small{font-size:11px;font-weight:500}
.pricing .btn{left:495px;top:473px}

/* testimonials */
.reviews{top:3757px;height:455px}
.reviews .title{position:absolute;top:80px;width:100%;text-align:center}
.review{position:absolute;top:150px;width:288px;height:218px;background:var(--tint-2);border-radius:14px;padding:30px 28px}
.stars{color:var(--star);font-size:14px;letter-spacing:3px}
.review p{margin-top:12px;font-size:12.4px;line-height:1.55;color:#333}
.review__who{position:absolute;left:28px;bottom:26px;display:flex;align-items:center;font-size:13.5px;font-weight:500;color:var(--ink)}
.avatar{width:40px;height:40px;border-radius:50%;margin-right:16px}
.quote{position:absolute;right:26px;bottom:26px;font-size:60px;font-weight:700;color:var(--sky-soft);line-height:36px;height:36px;overflow:hidden}
.arrow{position:absolute;top:242px;width:36px;height:36px;border-radius:50%;display:flex;align-items:center;justify-content:center}
.arrow--prev{left:76px;background:var(--tint-2)}
.arrow--next{left:1088px;background:var(--blue)}

footer{top:4212px;height:40px;background:var(--footer);color:#ddd;font-size:11.5px;text-align:center;line-height:40px}
</style>
</head>
<body>

<section class="hero">
  <div class="brand">POSTNOOK</div>
  <a class="btn btn--signup" href="#">Sign Up</a>
  <h1 class="hero__title">Your Voice, Your<br>Platform, Your Story</h1>
  <a class="btn" href="#">Sign Up For A Free Trial</a>
  <div class="art hero__art" role="img" aria-label="Illustration of a hand writing a blog post on a laptop among leaves"></div>
  <svg class="hero__wave" viewBox="0 0 1200 90" preserveAspectRatio="none">
    <path d="M0 45 C 300 90, 700 70, 1200 40 L1200 90 L0 90 Z" fill="#fff"/>
    <path d="M0 45 C 300 90, 700 70, 1200 40 L1200 44 C 700 76, 300 96, 0 52 Z" fill="#0054aa"/>
  </svg>
</section>

<section class="about">
  <div class="art about__art" role="img" aria-label="Illustration of a person designing a web page at a desktop screen"></div>
  <div class="about__body">
    <h2 class="title">ABOUT THE <em>PLATFORM</em></h2>
    <span class="rule"></span>
    <p>Lorem Ipsum is simply dummy text of the printing and typesetting industry. Lorem Ipsum has been the industry's standard dummy text ever since the 1500s, when an unknown printer took a galley of type and scrambled it to make a type specimen book. It has survived not only five centuries, but also the leap into electronic typesetting, remaining essentially unchanged. It was popularised in the 1960s with the release of Dryprint sheets containing Lorem Ipsum passages, and more recently with desktop publishing software like Folio Layout including versions of Lorem Ipsum.</p>
  </div>
  <a class="btn" href="#">Sign Up For A Free Trial</a>
</section>

<section class="how">
  <h2 class="title">HOW IT WORK<span class="rule"></span></h2>
  <p class="how__lead">The purpose of this platform is to allow anyone to start a blog and automate the process of creating content and posting it to the blog. Here is what the platform will consist of.</p>

  <div class="step" style="left:186px;top:238px">
    <div class="step__icon"><svg width="44" height="44" viewBox="0 0 44 44" fill="none" stroke="#0054aa" stroke-width="2"><circle cx="22" cy="18" r="14"/><circle cx="22" cy="14" r="5"/><path d="M13 27c3-5 15-5 18 0"/><rect x="11" y="35" width="22" height="6" rx="3"/></svg></div>
    <div class="step__name">Log in</div>
  </div>
  <div class="step" style="left:437px;top:238px">
    <div class="step__icon"><svg width="44" height="44" viewBox="0 0 44 44" fill="none" stroke="#0054aa" stroke-width="2"><rect x="7" y="8" width="30" height="22" rx="2"/><path d="M3 36h38M13 16h10M13 21h8M34 6l-10 14"/></svg></div>
    <div class="step__name">Create a new<br>blog post</div>
  </div>
  <div class="step" style="left:724px;top:238px">
    <div class="step__icon"><svg width="44" height="44" viewBox="0 0 44 44" fill="none" stroke="#0054aa" stroke-width="2"><rect x="6" y="5" width="32" height="34" rx="2"/><rect x="10" y="9" width="10" height="10"/><path d="M24 11h10M24 16h10M10 24h24M10 29h24M10 34h16"/></svg></div>
    <div class="step__name">Format and<br>optimize</div>
  </div>
  <div class="step" style="left:1010px;top:238px">
    <div class="step__icon"><svg width="44" height="44" viewBox="0 0 44 44" fill="none" stroke="#0054aa" stroke-width="2"><rect x="4" y="8" width="36" height="26" rx="2"/><path d="M4 14h36M14 28l22-10-14 4-2 8z"/></svg></div>
    <div class="step__name">Publish or<br>schedule</div>
  </div>
  <div class="step" style="left:310px;top:436px">
    <div class="step__icon"><svg width="44" height="44" viewBox="0 0 44 44" fill="none" stroke="#0054aa" stroke-width="2"><rect x="4" y="14" width="22" height="22" rx="2"/><rect x="18" y="5" width="22" height="18" rx="2"/><path d="M25 12l4 4 5-6M9 30l4-5 4 4 4-6"/></svg></div>
    <div class="step__name">Engage with<br>readers</div>
  </div>
  <div class="step" style="left:596px;top:436px">
    <div class="step__icon"><svg width="44" height="44" viewBox="0 0 44 44" fill="none" stroke="#0054aa" stroke-width="2"><rect x="4" y="6" width="36" height="26" rx="2"/><path d="M16 38h12M22 32v6M10 26v-6M16 26v-10M22 26v-4M28 18a5 5 0 1 0 6-6"/></svg></div>
    <div class="step__name">Monitor<br>performance</div>
  </div>
  <div class="step" style="left:883px;top:436px">
    <div class="step__icon"><svg width="44" height="44" viewBox="0 0 44 44" fill="none" stroke="#0054aa" stroke-width="2"><path d="M8 22a14 14 0 0 1 24-10M36 22a14 14 0 0 1-24 10M32 5v7h-7M12 39v-7h7"/><path d="M16 28v-5M22 28v-9M28 28v-6"/></svg></div>
    <div class="step__name">Adjust and<br>improve</div>
  </div>

  <a class="btn btn--light" href="#">Sign Up For A Free Trial</a>
</section>

<section class="benefits">
  <div class="benefits__body">
    <h2 class="title">BENEFITS OF <em>CONSISTENT<br>BLOGGING</em></h2>
    <span class="rule"></span>
  </div>
  <ul class="ticks" style="left:142px;top:200px">
    <li><svg width="14" height="14" viewBox="0 0 14 14" fill="none" stroke="#0094d4" stroke-width="1.6"><circle cx="7" cy="7" r="6"/><path d="M4 7l2 2 4-4"/></svg>Improved SEO</li>
    <li><svg width="14" height="14" viewBox="0 0 14 14" fill="none" stroke="#0094d4" stroke-width="1.6"><circle cx="7" cy="7" r="6"/><path d="M4 7l2 2 4-4"/></svg>Increased Authority</li>
    <li><svg width="14" height="14" viewBox="0 0 14 14" fill="none" stroke="#0094d4" stroke-width="1.6"><circle cx="7" cy="7" r="6"/><path d="M4 7l2 2 4-4"/></svg>Enhanced Engagement</li>
    <li><svg width="14" height="14" viewBox="0 0 14 14" fill="none" stroke="#0094d4" stroke-width="1.6"><circle cx="7" cy="7" r="6"/><path d="M4 7l2 2 4-4"/></svg>Content Variety</li>
    <li><svg width="14" height="14" viewBox="0 0 14 14" fill="none" stroke="#0094d4" stroke-width="1.6"><circle cx="7" cy="7" r="6"/><path d="M4 7l2 2 4-4"/></svg>Higher Conversion Rates</li>
  </ul>
  <ul class="ticks" style="left:352px;top:200px">
    <li><svg width="14" height="14" viewBox="0 0 14 14" fill="none" stroke="#0094d4" stroke-width="1.6"><circle cx="7" cy="7" r="6"/><path d="M4 7l2 2 4-4"/></svg>Brand Visibility</li>
    <li><svg width="14" height="14" viewBox="0 0 14 14" fill="none" stroke="#0094d4" stroke-width="1.6"><circle cx="7" cy="7" r="6"/><path d="M4 7l2 2 4-4"/></svg>Audience Insights</li>
    <li><svg width="14" height="14" viewBox="0 0 14 14" fill="none" stroke="#0094d4" stroke-width="1.6"><circle cx="7" cy="7" r="6"/><path d="M4 7l2 2 4-4"/></svg>Enhanced Social Media Presence</li>
    <li><svg width="14" height="14" viewBox="0 0 14 14" fill="none" stroke="#0094d4" stroke-width="1.6"><circle cx="7" cy="7" r="6"/><path d="M4 7l2 2 4-4"/></svg>Networking Opportunities</li>
    <li><svg width="14" height="14" viewBox="0 0 14 14" fill="none" stroke="#0094d4" stroke-width="1.6"><circle cx="7" cy="7" r="6"/><path d="M4 7l2 2 4-4"/></svg>Long-Term Benefits</li>
  </ul>
  <a class="btn" href="#">Sign Up For A Free Trial</a>
  <div class="art benefits__art" role="img" aria-label="Illustration of a person with a briefcase climbing a rising bar chart"></div>
</section>

<section class="seo">
  <div class="art seo__art" role="img" aria-label="Illustration of a person with a tablet beside a search page and a rocket"></div>
  <h2 class="title">SEO <em>VALUE</em><span class="rule"></span></h2>
  <ul class="ticks" style="left:642px;top:188px">
    <li><svg width="14" height="14" viewBox="0 0 14 14" fill="none" stroke="#0094d4" stroke-width="1.6"><circle cx="7" cy="7" r="6"/><path d="M4 7l2 2 4-4"/></svg>Fresh Content</li>
    <li><svg width="14" height="14" viewBox="0 0 14 14" fill="none" stroke="#0094d4" stroke-width="1.6"><circle cx="7" cy="7" r="6"/><path d="M4 7l2 2 4-4"/></svg>Keyword Optimization</li>
    <li><svg width="14" height="14" viewBox="0 0 14 14" fill="none" stroke="#0094d4" stroke-width="1.6"><circle cx="7" cy="7" r="6"/><path d="M4 7l2 2 4-4"/></svg>Increased Indexing</li>
    <li><svg width="14" height="14" viewBox="0 0 14 14" fill="none" stroke="#0094d4" stroke-width="1.6"><circle cx="7" cy="7" r="6"/><path d="M4 7l2 2 4-4"/></svg>Internal Linking</li>
    <li><svg width="14" height="14" viewBox="0 0 14 14" fill="none" stroke="#0094d4" stroke-width="1.6"><circle cx="7" cy="7" r="6"/><path d="M4 7l2 2 4-4"/></svg>Backlink Opportunities</li>
  </ul>
  <ul class="ticks" style="left:858px;top:188px">
    <li><svg width="14" height="14" viewBox="0 0 14 14" fill="none" stroke="#0094d4" stroke-width="1.6"><circle cx="7" cy="7" r="6"/><path d="M4 7l2 2 4-4"/></svg>Engagement Metrics</li>
    <li><svg width="14" height="14" viewBox="0 0 14 14" fill="none" stroke="#0094d4" stroke-width="1.6"><circle cx="7" cy="7" r="6"/><path d="M4 7l2 2 4-4"/></svg>Long-Tail Keywords</li>
    <li><svg width="14" height="14" viewBox="0 0 14 14" fill="none" stroke="#0094d4" stroke-width="1.6"><circle cx="7" cy="7" r="6"/><path d="M4 7l2 2 4-4"/></svg>Local SEO Benefits</li>
    <li><svg width="14" height="14" viewBox="0 0 14 14" fill="none" stroke="#0094d4" stroke-width="1.6"><circle cx="7" cy="7" r="6"/><path d="M4 7l2 2 4-4"/></svg>Enhanced User Experience</li>
    <li><svg width="14" height="14" viewBox="0 0 14 14" fill="none" stroke="#0094d4" stroke-width="1.6"><circle cx="7" cy="7" r="6"/><path d="M4 7l2 2 4-4"/></svg>Authority Building</li>
  </ul>
  <a class="btn" href="#">Sign Up For A Free Trial</a>
</section>

<section class="pricing">
  <h2 class="title">PRICING<span class="rule"></span></h2>
  <p class="pricing__lead">The platform can be used to sell unique accounts to multiple users. There must be a subscription plan and a 14-day free trial. The subscriptions are:</p>
  <div class="plans">
    <div class="plan">
      <div class="plan__name">Base Plan</div>
      <p class="plan__desc">1 blog post<br>(up to 2,000 words)<br>every month</p>
      <div class="plan__price">$9.99/<small>mo.</small></div>
    </div>
    <div class="plan">
      <div class="plan__name">Premium Plan</div>
      <p class="plan__desc">1 blog post<br>(up to 2,000 words)<br>every week</p>
      <div class="plan__price">$14.99/<small>mo.</small></div>
    </div>
    <div class="plan">
      <div class="plan__name">Ultimate Plan</div>
      <p class="plan__desc">1 blog post<br>(up to 3,000 words)<br>per day plus unlimited<br>manual posting</p>
      <div class="plan__price">$24.99/<small>mo.</small></div>
    </div>
  </div>
  <a class="btn btn--light" href="#">Sign Up For A Free Trial</a>
</section>

<section class="reviews">
  <h2 class="title">LET'S SEE OUR <em>CUSTOMER SAY</em></h2>
  <a class="arrow arrow--prev" href="#"><svg width="12" height="12" viewBox="0 0 12 12" fill="none" stroke="#0054aa" stroke-width="2"><path d="M8 2L4 6l4 4"/></svg></a>

  <article class="review" style="left:142px">
    <div class="stars">★★★★★</div>
    <p>Lorem ipsum dolor sit amet, consectetur adipiscing elit. Proin suscipit metus tellus, at ultricies libero pulvinar sit amet.</p>
    <div class="review__who"><span class="avatar" role="img" aria-label="Portrait photo of Maya Ortiz" style="background:#8a6a55"></span>Maya Ortiz</div>
    <span class="quote">”</span>
  </article>
  <article class="review" style="left:455px">
    <div class="stars">★★★★★</div>
    <p>Lorem ipsum dolor sit amet, consectetur adipiscing elit. Proin suscipit metus tellus, at ultricies libero pulvinar sit amet.</p>
    <div class="review__who"><span class="avatar" role="img" aria-label="Portrait photo of Jordan Pike" style="background:#9cc6dd"></span>Jordan Pike</div>
    <span class="quote">”</span>
  </article>
  <article class="review" style="left:769px">
    <div class="stars">★★★★★</div>
    <p>Lorem ipsum dolor sit amet, consectetur adipiscing elit. Proin suscipit metus tellus, at ultricies libero pulvinar sit amet.</p>
    <div class="review__who"><span class="avatar" role="img" aria-label="Portrait photo of Riley Hart" style="background:#6b4a3a"></span>Riley Hart</div>
    <span class="quote">”</span>
  </article>

  <a class="arrow arrow--next" href="#"><svg width="12" height="12" viewBox="0 0 12 12" fill="none" stroke="#fff" stroke-width="2"><path d="M4 2l4 4-4 4"/></svg></a>
</section>

<footer>© 2024 PostNook. All Rights Reserved.</footer>

</body>
</html>
```